Business card design needed

We do excavation, cartage and contracting
I would quote like to have a picture of my digger as the whole back ground and the words on top. If that looks any good
Otherwise please feel free to come up with any other cool options

Cheers Marc

KLR Contracting
Excavation, Cartage, Contracting
Marcus Prewitt
www.klr-example.co.nz
021 584 067
marc@klr-example.co.nz

```html
<!DOCTYPE html>
<html lang="en">
<head>
<meta charset="utf-8">
<title>KLR Contracting – Business Cards</title>
<link href="https://fonts.googleapis.com/css2?family=Cinzel:wght@400;600&display=swap" rel="stylesheet">
<style>
  :root {
    --page-bg: #e9e6e2;
    --green: #1f5b1c;
    --green-dark: #174a15;
    --tan: #b9822f;
    --ink-dark: #1e2410;
    --white: #ffffff;
    --sky-top: #ffffff;
    --sky-bottom: #c9dbe9;
    --link-blue: #c4dcee;
    --machine-yellow: #e0b23c;
    --machine-earth: #8f7d58;
  }
  * { margin: 0; padding: 0; box-sizing: border-box; }
  html, body { width: 1200px; height: 868px; overflow: hidden; }
  body {
    background: var(--page-bg);
    font-family: "Cinzel", "Times New Roman", serif;
    position: relative;
  }
  .card {
    position: absolute;
    top: 284px;
    width: 520px;
    height: 300px;
    border-radius: 14px;
    overflow: hidden;
    box-shadow: 0 6px 18px rgba(0,0,0,0.18);
  }
  /* Back of card */
  .card-back {
    left: 50px;
    background: linear-gradient(180deg, var(--green) 0%, var(--green-dark) 100%);
    color: var(--white);
    display: flex;
    flex-direction: column;
    align-items: center;
    justify-content: center;
  }
  .brand-name {
    font-weight: 600;
    font-size: 96px;
    letter-spacing: 4px;
    line-height: 1;
  }
  .brand-tag {
    margin-top: 18px;
    font-size: 32px;
    letter-spacing: 4px;
  }
  /* Front of card */
  .card-front {
    left: 630px;
    background: linear-gradient(180deg, var(--sky-top) 0%, var(--sky-bottom) 100%);
  }
  .front-band {
    position: absolute;
    left: 0; right: 0; bottom: 0;
    height: 155px;
    background: var(--green);
  }
  .service-panel {
    position: absolute;
    left: 0; top: 0;
    width: 520px; height: 300px;
  }
  .machine-photo {
    position: absolute;
    left: 176px;
    top: 12px;
    width: 332px;
    height: 128px;
    border-radius: 6px;
    background: linear-gradient(135deg, var(--machine-yellow) 0%, #c99c34 55%, var(--machine-earth) 100%);
  }
  .front-logo {
    position: absolute;
    left: 38px;
    top: 44px;
    font-size: 40px;
    font-weight: 600;
    color: var(--green);
    letter-spacing: 2px;
  }
  .services {
    position: absolute;
    left: 22px;
    bottom: 16px;
    font-size: 14px;
    color: var(--ink-dark);
    line-height: 1.35;
    letter-spacing: 0.5px;
  }
  .services span { display: block; }
  .services span:nth-child(2) { padding-left: 26px; }
  .services span:nth-child(3) { padding-left: 6px; }
  .contact {
    position: absolute;
    right: 24px;
    top: 160px;
    text-align: right;
    color: var(--white);
  }
  .contact-name {
    font-size: 19px;
    letter-spacing: 1.5px;
  }
  .contact-line {
    font-size: 10.5px;
    letter-spacing: 0.5px;
    line-height: 1.35;
  }
  .contact-phone { margin-top: 16px; }
  .contact-web {
    margin-top: 18px;
    font-size: 15px;
    letter-spacing: 1px;
    color: var(--link-blue);
  }
</style>
</head>
<body>

  <section class="card card-back" aria-label="Card back">
    <div class="brand-name">KLR</div>
    <div class="brand-tag">Contracting</div>
  </section>

  <section class="card card-front" aria-label="Card front">
    <div class="front-band"></div>

    <svg class="service-panel" viewBox="0 0 520 300" aria-hidden="true">
      <polygon points="0,214 132,180 188,300 0,300" fill="var(--tan)"/>
    </svg>

    <div class="machine-photo" role="img" aria-label="Photo of a yellow excavator with its arm reaching out and bucket lowered"></div>

    <div class="front-logo">KLR</div>

    <div class="services">
      <span>Excavation</span>
      <span>Cartage</span>
      <span>Contracting</span>
    </div>

    <div class="contact">
      <div class="contact-name">Marcus Prewitt</div>
      <div class="contact-line contact-phone">021 584 067</div>
      <div class="contact-line">marc@klr-example.co.nz</div>
      <div class="contact-web">www.klr-example.co.nz</div>
    </div>
  </section>

</body>
</html>
```